Palisade Lift Inc Website Deisgn

We are a new small elevator contracting company.
We would like a full website designed similar to
http://brightmorelift.com or https://www.northpeaklifting.ca/
In addition to contents found on the above webpages.. we would like a section for project gallery etc.... have fun with it ... make it professional

Target Market(s)

Elevator Consultants - Property managers - Condo Boards - Commercial office buildings

Coding

Coded - Design and coding required

Number of Pages Required

5+ page

Requirements
Must have
• Navigation Bar.. Be view able via mobile ..Should be pictures of Tall Office buildings in background.. Toronto city skyline etc....

Have Fun!

```html
<!DOCTYPE html>
<html lang="en">
<head>
<meta charset="utf-8">
<title>Palisade Lift Inc</title>
<link href="https://fonts.googleapis.com/css2?family=Bebas+Neue&family=Lato:wght@400;700&display=swap" rel="stylesheet">
<style>
:root{
  --blue:#4a7ab5;
  --ink:#2b2b2b;
  --text:#555;
  --muted:#777;
  --line:#dcdcdc;
  --band:#f1f1f1;
  --footer:#333;
  --footer-low:#2a2a2a;
  --white:#fff;
}
*{box-sizing:border-box;margin:0;padding:0}
html,body{width:1200px;height:3699px;overflow:hidden;background:var(--white)}
body{font-family:"Lato",sans-serif;color:var(--text);font-size:13px;line-height:1.35}
.page{position:relative;width:1200px;height:3699px;overflow:hidden}
.abs{position:absolute}
.heading{font-family:"Bebas Neue",sans-serif;color:var(--ink);letter-spacing:1px;font-weight:400}
.btn{position:absolute;display:flex;align-items:center;justify-content:center;background:var(--blue);color:var(--white);border-radius:20px;font-size:13px}
.media{position:absolute}

/* header */
.brand{left:75px;top:28px;font-size:30px;font-weight:700;color:var(--ink);display:flex;align-items:center;gap:10px;letter-spacing:.5px}
.brand .dot{width:14px;height:14px;border-radius:50%;background:var(--ink)}
.nav{left:537px;top:38px;display:flex;gap:30px;font-size:14px;color:#555}
.nav .active{color:var(--blue);border-bottom:2px solid var(--blue);padding-bottom:4px}

/* hero */
.hero{left:0;top:100px;width:1200px;height:600px;background:linear-gradient(100deg,#c9cdd1 0%,#8c96a0 30%,#2d4468 55%,#6f7b86 75%,#b9bec2 100%)}
.hero-title{left:0;width:1200px;top:338px;text-align:center;font-size:34px;color:var(--white);letter-spacing:2px}
.hero-text{left:0;width:1200px;top:382px;text-align:center;color:var(--white);font-size:12px}
.arrow-tab{width:36px;height:36px;background:rgba(255,255,255,.35);top:383px;display:flex;align-items:center;justify-content:center}
.dots{left:574px;top:658px;display:flex;gap:8px}
.dots span{width:9px;height:9px;border:1px solid var(--white);border-radius:50%}
.dots span:first-child{background:var(--white)}

/* about */
.about-title{left:112px;top:790px;font-size:30px}
.about-rule{left:90px;top:828px;width:46px;height:3px;background:var(--blue)}
.about-text{left:113px;top:848px;width:445px;font-size:12px}
.about-text p{margin-bottom:14px}

/* services */
.center-title{left:0;width:1200px;text-align:center}
.svc{position:absolute;top:1299px;width:247px;height:219px;border:1px solid var(--line);padding:112px 20px 0 20px;background:var(--white)}
.svc h3{position:absolute;top:82px;left:20px;font-size:18px;font-weight:700;color:var(--ink);letter-spacing:.5px}
.svc h3::after{content:"";display:block;width:62px;height:2px;background:var(--ink);margin-top:6px}
.svc p{font-size:12px;color:var(--muted);margin-top:18px}
.svc svg.icon{position:absolute;left:20px;top:16px}
.svc .go{position:absolute;left:20px;bottom:16px}
.svc.featured{background:var(--blue);border-color:var(--blue);box-shadow:0 4px 10px rgba(0,0,0,.2)}
.svc.featured h3,.svc.featured p{color:var(--white)}
.svc.featured h3::after{background:var(--white)}

/* gallery */
.gallery-band{left:0;top:1639px;width:1200px;height:628px;background:var(--band)}
.tile{position:absolute}
.project-caption{position:absolute;left:22px;top:292px;color:var(--white);font-size:12px}
.project-caption h4{font-family:"Bebas Neue",sans-serif;font-size:15px;letter-spacing:1px;font-weight:400}
.project-caption h4::after{content:"";display:block;width:44px;height:1px;background:var(--white);margin:4px 0 8px}

/* news */
.news{position:absolute;top:2378px;width:331px;height:413px;border:1px solid var(--line);padding:14px}
.news .photo{width:301px;height:214px}
.news h4{font-family:"Bebas Neue",sans-serif;font-size:17px;color:var(--ink);font-weight:400;letter-spacing:1px;margin:24px 0 6px 6px}
.meta{display:flex;gap:8px;align-items:center;font-size:12px;color:var(--muted);margin-left:6px}
.news p{font-size:12px;color:var(--muted);margin:10px 6px 0}
.news .more{font-size:12px;color:var(--muted);margin:18px 6px 0;display:flex;align-items:center;gap:3px}

/* faq */
.faq{position:absolute;left:633px;width:493px;height:38px;border:1px solid #c9c9c9;display:flex;align-items:center;justify-content:space-between;padding:0 14px;font-size:12px;color:#555}

/* footer */
.footer{left:0;top:3358px;width:1200px;height:341px;background:var(--footer);color:#ddd}
.footer-base{left:0;top:3627px;width:1200px;height:72px;background:var(--footer-low)}
.f-title{position:absolute;font-family:"Bebas Neue",sans-serif;color:var(--white);font-size:17px;letter-spacing:1px}
.f-title::after{content:"";display:block;width:48px;height:2px;background:var(--white);margin-top:4px}
.f-list{position:absolute;list-style:none;font-size:13px;line-height:22.5px;color:#eee}
.f-list li::before{content:"•";margin-right:8px}
.contact{position:absolute;left:603px;top:3459px;font-size:12.5px;color:#eee;line-height:25px}
.contact div{display:flex;gap:12px;align-items:center}
.social{position:absolute;top:3643px;width:34px;height:34px;border-radius:50%;background:var(--white)}
</style>
</head>
<body>
<div class="page">

  <!-- header -->
  <div class="abs brand"><span class="dot"></span>Palisade Lift Inc</div>
  <nav class="abs nav">
    <span class="active">Home</span><span>About</span><span>Services ⌄</span><span>Galery</span><span>News</span><span>Contact us</span>
  </nav>
  <div class="btn" style="left:982px;top:28px;width:148px;height:38px">Get a Quote</div>

  <!-- hero -->
  <div class="abs hero" role="img" aria-label="Businessman in a blue suit stepping into a glass elevator"></div>
  <h1 class="abs heading hero-title">Be Safe With Us</h1>
  <p class="abs hero-text">Lorem Ipsum is simply dummy text of the printing<br>in thenext typesetting industry.</p>
  <div class="btn" style="left:521px;top:426px;width:166px;height:38px">Read More</div>
  <div class="abs arrow-tab" style="left:0"><svg width="18" height="10"><path d="M17 5H2M6 1L2 5l4 4" stroke="#fff" stroke-width="1.6" fill="none"/></svg></div>
  <div class="abs arrow-tab" style="left:1164px"><svg width="18" height="10"><path d="M1 5h15M12 1l4 4-4 4" stroke="#fff" stroke-width="1.6" fill="none"/></svg></div>
  <div class="abs dots"><span></span><span></span><span></span><span></span></div>

  <!-- about -->
  <h2 class="abs heading about-title">About Us</h2>
  <div class="abs about-rule"></div>
  <div class="abs about-text">
    <p>Lorem Ipsum is simply dummy text of the printing and typesetting industry has been the industry's standard dummy text ever since the 1500s,</p>
    <p>when an unknown printer took a galley of type and scrambled it to make an type specimen book. It has survived not only five centuries, but also the leap into electronic typesetting, remaining essentially unchanged. It popularised in the 1960s</p>
    <p>with the release of Tessaprint sheets containing Lorem Ipsum passages, and more recently with desktop publishing software Corvel LayoutDesk including versions of Lorem Ipsum.</p>
  </div>
  <div class="btn" style="left:112px;top:1044px;width:164px;height:38px">Read More</div>
  <div class="media" style="left:601px;top:700px;width:599px;height:448px;background:linear-gradient(180deg,#e9ecef 0%,#d9dde2 55%,#9aa7b4 80%,#c6cbcf 100%)" role="img" aria-label="Toronto city skyline with the CN Tower across the water"></div>
  <div class="media" style="left:488px;top:1033px;width:228px;height:152px;background:linear-gradient(120deg,#d9a34a 0%,#5b6672 40%,#2f3a48 100%)" role="img" aria-label="Technician in a hard hat servicing elevator machinery"></div>

  <!-- services -->
  <h2 class="abs heading center-title" style="top:1214px;font-size:30px">Services</h2>
  <svg class="abs" style="left:568px;top:1250px" width="66" height="14"><line x1="0" y1="7" x2="24" y2="7" stroke="#333"/><circle cx="33" cy="7" r="6" fill="none" stroke="#333"/><line x1="42" y1="7" x2="66" y2="7" stroke="#333"/></svg>
  <p class="abs center-title" style="top:1267px;font-size:13px">Lorem Ipsum is simply dummy.</p>

  <div class="svc" style="left:75px">
    <svg class="icon" width="48" height="52" fill="none" stroke="#222" stroke-width="1.5"><rect x="2" y="6" width="44" height="44"/><rect x="8" y="12" width="32" height="38"/><line x1="24" y1="12" x2="24" y2="50"/><rect x="16" y="1" width="16" height="5"/></svg>
    <h3>Elevator</h3>
    <p>Lorem Ipsum is simply dummy and text of the printing and typesetting in the industry.</p>
    <svg class="go" width="18" height="10"><path d="M1 5h15M12 1l4 4-4 4" stroke="#4a7ab5" stroke-width="1.6" fill="none"/></svg>
  </div>
  <div class="svc featured" style="left:343px">
    <svg class="icon" width="56" height="56" fill="none" stroke="#fff" stroke-width="1.5"><circle cx="28" cy="28" r="24"/><circle cx="28" cy="28" r="15"/><circle cx="28" cy="28" r="6"/></svg>
    <h3>Modernization</h3>
    <p>Lorem Ipsum is simply dummy and text of the printing and typesetting in the industry.</p>
    <svg class="go" width="18" height="10"><path d="M1 5h15M12 1l4 4-4 4" stroke="#fff" stroke-width="1.6" fill="none"/></svg>
  </div>
  <div class="svc" style="left:611px">
    <svg class="icon" width="54" height="58" fill="none" stroke="#222" stroke-width="1.5"><circle cx="27" cy="14" r="9"/><path d="M8 56V40q0-10 19-10t19 10v16"/><path d="M4 8l10 10M50 8L40 18"/></svg>
    <h3>Services &amp; Repair</h3>
    <p>Lorem Ipsum is simply dummy and text of the printing and typesetting in the industry.</p>
    <svg class="go" width="18" height="10"><path d="M1 5h15M12 1l4 4-4 4" stroke="#4a7ab5" stroke-width="1.6" fill="none"/></svg>
  </div>
  <div class="svc" style="left:880px">
    <svg class="icon" width="56" height="60" fill="none" stroke="#222" stroke-width="1.5"><rect x="2" y="6" width="40" height="52"/><line x1="22" y1="6" x2="22" y2="58"/><rect x="12" y="1" width="20" height="5"/><path d="M50 22l3 4h-6zM50 38l3-4h-6z"/></svg>
    <h3>Installation</h3>
    <p>Lorem Ipsum is simply dummy and text of the printing and typesetting in the industry.</p>
    <svg class="go" width="18" height="10"><path d="M1 5h15M12 1l4 4-4 4" stroke="#4a7ab5" stroke-width="1.6" fill="none"/></svg>
  </div>
  <div class="btn" style="left:521px;top:1558px;width:166px;height:38px">View More</div>

  <!-- gallery -->
  <div class="abs gallery-band"></div>
  <h2 class="abs heading center-title" style="top:1675px;font-size:30px">Our Gallery</h2>
  <p class="abs center-title" style="top:1712px;font-size:13px">Lorem Ipsum is simply dummy of the printing</p>
  <div class="tile" style="left:74px;top:1745px;width:247px;height:187px;background:linear-gradient(135deg,#d8d4cc,#8a8377 60%,#3a3632)" role="img" aria-label="Glass elevator in a modern atrium"></div>
  <div class="tile" style="left:74px;top:1954px;width:247px;height:187px;background:linear-gradient(160deg,#dfe6f2,#8799b8 55%,#3d4a63)" role="img" aria-label="Tall building atrium with elevator shafts"></div>
  <div class="tile" style="left:343px;top:1745px;width:247px;height:396px;background:linear-gradient(180deg,#9a9894,#6c6a66 60%,#4a4946)" role="img" aria-label="Closed steel elevator doors in a lobby">
    <div class="project-caption"><h4>Projects Name</h4>Lorem Ipsum is a simply dummy text<br>of the printing.<br><svg width="18" height="10" style="margin-top:8px"><path d="M1 5h15M12 1l4 4-4 4" stroke="#fff" stroke-width="1.6" fill="none"/></svg></div>
  </div>
  <div class="tile" style="left:611px;top:1745px;width:247px;height:187px;background:linear-gradient(90deg,#2c2c2c,#bdbdbd 50%,#2c2c2c)" role="img" aria-label="Long corridor with elevator doors"></div>
  <div class="tile" style="left:611px;top:1954px;width:247px;height:187px;background:linear-gradient(135deg,#c9cdc9,#2f7a4e 50%,#3b3f3c)" role="img" aria-label="Green elevator hoist machinery"></div>
  <div class="tile" style="left:880px;top:1745px;width:248px;height:396px;background:linear-gradient(180deg,#6c7a86,#cfd6dc 45%,#4a5866)" role="img" aria-label="Cylindrical glass panoramic elevator"></div>
  <div class="btn" style="left:521px;top:2177px;width:166px;height:38px">View More</div>

  <!-- news -->
  <h2 class="abs heading center-title" style="top:2326px;font-size:30px">Latest News</h2>
  <article class="news" style="left:75px">
    <div class="photo" style="background:linear-gradient(180deg,#d9d6d0,#9c8c78 55%,#3f3d3b)" role="img" aria-label="Modern lobby with elevator doors"></div>
    <h4>Title Heading 01</h4>
    <div class="meta"><span>▦ 3-17-2020</span><span>|</span><span>◯ Martin Kessler</span></div>
    <p>Lorem Ipsum is simply dummy text of the printing a setting industry orem Ipsum has been the industry text ever since the 1500s,</p>
    <div class="more">Read More.. <svg width="12" height="12"><circle cx="6" cy="6" r="5" fill="none" stroke="#777"/><path d="M5 3.5L7.5 6 5 8.5" stroke="#777" fill="none"/></svg></div>
  </article>
  <article class="news" style="left:436px">
    <div class="photo" style="background:linear-gradient(90deg,#2a2f33,#8f9893 50%,#2a2f33)" role="img" aria-label="Woman looking out a tall office window over the city"></div>
    <h4>Title Heading 01</h4>
    <div class="meta"><span>▦ 3-17-2020</span><span>|</span><span>◯ Martin Kessler</span></div>
    <p>Lorem Ipsum is simply dummy text of the printing a setting industry orem Ipsum has been the industry text ever since the 1500s,</p>
    <div class="more">Read More.. <svg width="12" height="12"><circle cx="6" cy="6" r="5" fill="none" stroke="#777"/><path d="M5 3.5L7.5 6 5 8.5" stroke="#777" fill="none"/></svg></div>
  </article>
  <article class="news" style="left:798px">
    <div class="photo" style="background:linear-gradient(110deg,#2d4468,#6f7f92 55%,#e7a04a)" role="img" aria-label="Businessman pressing an elevator button"></div>
    <h4>Title Heading 01</h4>
    <div class="meta"><span>▦ 3-17-2020</span><span>|</span><span>◯ Martin Kessler</span></div>
    <p>Lorem Ipsum is simply dummy text of the printing a setting industry orem Ipsum has been the industry text ever since the 1500s,</p>
    <div class="more">Read More.. <svg width="12" height="12"><circle cx="6" cy="6" r="5" fill="none" stroke="#777"/><path d="M5 3.5L7.5 6 5 8.5" stroke="#777" fill="none"/></svg></div>
  </article>
  <div class="btn" style="left:521px;top:2823px;width:166px;height:38px">View More</div>

  <!-- faq -->
  <h2 class="abs heading center-title" style="top:2905px;font-size:32px;letter-spacing:2px">Frequently Asked Question</h2>
  <div class="media" style="left:0;top:2972px;width:601px;height:386px;background:linear-gradient(120deg,#e39a2c 0%,#2f5f9c 35%,#7b8a96 70%,#c9c34a 100%)" role="img" aria-label="Technician in an orange hard hat working on an elevator control panel"></div>
  <div class="faq" style="top:2978px">Lorem simply dummy text of the?<svg width="13" height="13"><circle cx="6.5" cy="6.5" r="6.5" fill="#4a7ab5"/><path d="M5.5 4l2.5 2.5L5.5 9" stroke="#fff" fill="none" stroke-width="1.4"/></svg></div>
  <div class="faq" style="top:3030px">Lorem Ipsum the printing and industry<svg width="13" height="13"><circle cx="6.5" cy="6.5" r="6.5" fill="#4a7ab5"/><path d="M5.5 4l2.5 2.5L5.5 9" stroke="#fff" fill="none" stroke-width="1.4"/></svg></div>
  <div class="faq" style="top:3081px">Lorem Ipsum is simply industry. Lorem ?<svg width="13" height="13"><circle cx="6.5" cy="6.5" r="6.5" fill="#4a7ab5"/><path d="M5.5 4l2.5 2.5L5.5 9" stroke="#fff" fill="none" stroke-width="1.4"/></svg></div>
  <div class="faq" style="top:3133px">Lorem and typesetting industry ?<svg width="13" height="13"><circle cx="6.5" cy="6.5" r="6.5" fill="#4a7ab5"/><path d="M5.5 4l2.5 2.5L5.5 9" stroke="#fff" fill="none" stroke-width="1.4"/></svg></div>
  <div class="faq" style="top:3185px">Lorem Ipsum is simply industry. Lorem ?<svg width="13" height="13"><circle cx="6.5" cy="6.5" r="6.5" fill="#4a7ab5"/><path d="M5.5 4l2.5 2.5L5.5 9" stroke="#fff" fill="none" stroke-width="1.4"/></svg></div>
  <div class="faq" style="top:3236px">Lorem Ipsum is simply text of the printing<svg width="13" height="13"><circle cx="6.5" cy="6.5" r="6.5" fill="#4a7ab5"/><path d="M5.5 4l2.5 2.5L5.5 9" stroke="#fff" fill="none" stroke-width="1.4"/></svg></div>
  <div class="faq" style="top:3286px">Lorem and typesetting industry ?<svg width="13" height="13"><circle cx="6.5" cy="6.5" r="6.5" fill="#4a7ab5"/><path d="M5.5 4l2.5 2.5L5.5 9" stroke="#fff" fill="none" stroke-width="1.4"/></svg></div>

  <!-- footer -->
  <footer class="abs footer"></footer>
  <div class="abs footer-base"></div>
  <div class="abs" style="left:115px;top:3420px;font-size:28px;font-weight:700;color:#fff;display:flex;align-items:center;gap:10px"><span style="width:14px;height:14px;border-radius:50%;background:#fff"></span>Palisade Lift Inc</div>
  <p class="abs" style="left:115px;top:3489px;width:240px;font-size:12.5px;color:#eee">Lorem Ipsum is simply dummy text next of the printing and typesetting industry has been the industry's</p>
  <svg class="abs" style="left:115px;top:3563px" width="18" height="10"><path d="M1 5h15M12 1l4 4-4 4" stroke="#fff" stroke-width="1.6" fill="none"/></svg>

  <div class="f-title" style="left:432px;top:3405px">Quick Link</div>
  <ul class="f-list" style="left:433px;top:3446px">
    <li>Home</li><li>About us</li><li>Services</li><li>Gallery</li><li>News</li><li>Contact us</li>
  </ul>

  <div class="f-title" style="left:602px;top:3405px">Quick Contact</div>
  <div class="contact">
    <div><svg width="11" height="14"><path d="M5.5 13S1 8 1 5a4.5 4.5 0 019 0c0 3-4.5 8-4.5 8z" fill="none" stroke="#ddd"/><circle cx="5.5" cy="5" r="1.6" fill="#ddd"/></svg>88 Harbourline Road</div>
    <div style="padding-left:23px">Maple Ridge, Alberta</div>
    <div><svg width="12" height="11"><rect x=".5" y="2" width="11" height="8" rx="1" fill="none" stroke="#ddd"/><rect x="3" y=".5" width="6" height="3" fill="none" stroke="#ddd"/></svg>647 555 0142</div>
    <div><svg width="12" height="11"><rect x=".5" y="2" width="11" height="8" rx="1" fill="none" stroke="#ddd"/><rect x="3" y=".5" width="6" height="3" fill="none" stroke="#ddd"/></svg>905 555 0187</div>
    <div><svg width="12" height="10"><rect x=".5" y=".5" width="11" height="9" fill="none" stroke="#ddd"/><path d="M.5 .5L6 5.5 11.5 .5" fill="none" stroke="#ddd"/></svg>info@palisadelift.co</div>
  </div>

  <div class="f-title" style="left:857px;top:3405px">Subscribe</div>
  <p class="abs" style="left:858px;top:3449px;width:240px;font-size:12.5px;color:#eee">Lorem Ipsum is simply dummy text next of the printing and typesetting.</p>
  <div class="abs" style="left:857px;top:3495px;width:232px;height:32px;border-radius:16px;background:#fff;padding:8px 16px;font-size:12.5px;color:#555">Email Here</div>
  <div class="btn" style="left:857px;top:3538px;width:232px;height:32px;letter-spacing:1px">Send Now</div>

  <p class="abs" style="left:110px;top:3654px;font-size:12.5px;color:#ddd">Copyright © 2020 Palisade Lift Inc. All Right Reserved</p>
  <span class="social" style="left:873px"></span>
  <span class="social" style="left:918px"></span>
  <span class="social" style="left:963px"></span>
  <span class="social" style="left:1008px"></span>
  <span class="social" style="left:1053px"></span>
</div>
</body>
</html>
```